Brava Set CEO and Partners Business Card

We need a fresh, fun, simple and clean business card design....we would like a template where we can add a name and title (as well as specific email addresses). We are open to different looks (full logo on one side and a small logo on the company info side, or our logo is in the background but faint on one side but full on the other, or something else cool :-) ). Our colors are in our logo: blue, black and white...however we are not opposed to the use of other colors if it works. We build sets, make props and a host of other things for the film and television industry...our card should reflect creativity, style and professionalism.

A white background would be preferred.

I would like to see an option with Facebook and Instagram icons.

Facebook- facebook.com/bravasetny
Instagram- brava_set

Our website is bravaset-example.com.

Brava Set, Inc.
418 Corvell Avenue, Unit 9
North Hollywood, California 91602
555.210.4873 | tel
555.210.6692 | fax
www.BravaSet-example.com

Sample Name and Title #1:

Peter Halvik
CEO / Co-Owner
555.210.4873 | tel
555.210.6692 | fax
peter@bravaset-example.com
www.BravaSet-example.com

Target Market(s)

Marketing Professionals, Production Designers, Interior Designers, Film Producers, Directors, Art Directors, Event Directors

Industry/Entity Type

Entertainment Industry

Contact Information for Business Card

Peter Halvik
CEO / Co-Owner
555.210.4873 | tel
555.210.6692 | fax
peter@bravaset-example.com
www.BravaSet-example.com

Font styles to use
Sans Serif

Colors
33a6d7
ffffff
1b1b1b

Requirements
Must have
• Logo, All Contact Info, White Background. Symmetry.
Nice to have
• Facebook and Instagram icons with addresses
• Facebook- facebook.com/bravasetny
• Instagram- brava_set

```html
<!DOCTYPE html>
<html lang="en">
<head>
<meta charset="utf-8">
<title>Brava Set – Business Card</title>
<link rel="stylesheet" href="https://fonts.googleapis.com/css2?family=Open+Sans:wght@400;600;800&display=swap">
<style>
  :root {
    --brand-blue: #29a6df;
    --ink: #1b1b1b;
    --text-grey: #4a4a4a;
    --paper: #ffffff;
    --backdrop: #e8e5e1;
  }
  * { margin: 0; padding: 0; box-sizing: border-box; }
  html, body {
    width: 1200px; height: 987px; overflow: hidden;
    background: var(--backdrop);
    font-family: "Open Sans", sans-serif;
  }
  .canvas { position: relative; width: 1200px; height: 987px; }

  .card {
    position: absolute; left: 293px; width: 615px; height: 352px;
    box-shadow: 0 2px 6px rgba(0,0,0,.25);
  }

  /* Front side */
  .card-front { top: 130px; background: var(--paper); }
  .card-front .wordmark {
    position: absolute; right: 31px; top: 34px;
    font-size: 52px; font-weight: 800; letter-spacing: -1px;
    color: var(--ink); line-height: 1;
  }
  .holder-name {
    position: absolute; left: 27px; top: 160px;
    font-size: 22px; font-weight: 600; color: var(--brand-blue);
  }
  .holder-title {
    position: absolute; left: 27px; top: 188px;
    font-size: 16px; color: var(--ink);
  }
  .divider {
    position: absolute; left: 27px; right: 31px; top: 215px;
    height: 1px; background: var(--ink);
  }
  .contact-list { position: absolute; left: 32px; top: 224px; list-style: none; }
  .contact-list li {
    display: flex; align-items: center; height: 23.5px;
    font-size: 15px; color: var(--text-grey);
  }
  .contact-list svg { width: 15px; height: 15px; margin-right: 7px; fill: var(--brand-blue); }
  .address {
    position: absolute; right: 31px; top: 248px; text-align: right;
    font-size: 15px; line-height: 23.5px; color: var(--text-grey); font-style: normal;
  }
  .edge-line {
    position: absolute; left: 0; right: 0; top: 334px; height: 2px; background: var(--ink);
  }
  .edge-band {
    position: absolute; left: 0; right: 0; top: 339px; height: 13px; background: var(--brand-blue);
  }

  /* Back side */
  .card-back { top: 505px; background: var(--brand-blue); }
  .card-back .wordmark {
    position: absolute; left: 0; right: 0; top: 140px; text-align: center;
    font-size: 66px; font-weight: 800; letter-spacing: -1px;
    color: var(--paper); line-height: 1;
  }
  .social {
    position: absolute; left: 0; right: 0; top: 292px;
    display: flex; justify-content: center; gap: 14px;
    font-size: 16px; color: var(--paper);
  }
  .social span { display: flex; align-items: center; }
  .social .marker {
    width: 16px; height: 16px; background: var(--paper); margin-right: 5px; border-radius: 2px;
  }
</style>
</head>
<body>
<main class="canvas">

  <section class="card card-front" aria-label="Business card front">
    <div class="wordmark">Brava Set</div>
    <h1 class="holder-name">Peter Halvik</h1>
    <p class="holder-title">CEO / Co-Owner</p>
    <div class="divider"></div>
    <ul class="contact-list">
      <li>
        <svg viewBox="0 0 16 16" aria-hidden="true"><path d="M3.6 1.2l2.3 2.6-1.3 1.7c.9 2 2.4 3.5 4.4 4.4l1.7-1.3 2.6 2.3-1.4 2.3C7.2 13.4 2.6 8.8 1.4 3z"/></svg>
        555.210.4873
      </li>
      <li>
        <svg viewBox="0 0 16 16" aria-hidden="true"><path d="M4 1h6l2 2v3H4z M1 7h14v6h-2v-2H3v2H1z M4 12h8v3H4z"/></svg>
        555.210.6692
      </li>
      <li>
        <svg viewBox="0 0 16 16" aria-hidden="true"><path d="M1 3h14v10H1z" fill="none" stroke="#29a6df" stroke-width="1.6"/><path d="M1.5 3.5L8 9l6.5-5.5" fill="none" stroke="#29a6df" stroke-width="1.6"/></svg>
        peter@bravaset-example.com
      </li>
      <li>
        <svg viewBox="0 0 16 16" aria-hidden="true"><circle cx="8" cy="8" r="7"/><path d="M5 4c2 1 1 3 3 3s1 3 3 3M9 2c0 2 3 2 4 4" fill="none" stroke="#fff" stroke-width="1.3"/></svg>
        www.BravaSet-example.com
      </li>
    </ul>
    <address class="address">
      418 Corvell Avenue<br>
      Unit 9, North Hollywood<br>
      California 91602
    </address>
    <div class="edge-line"></div>
    <div class="edge-band"></div>
  </section>

  <section class="card card-back" aria-label="Business card back">
    <div class="wordmark">Brava Set</div>
    <div class="social">
      <span><i class="marker"></i>bravasetny</span>
      <span><i class="marker"></i>brava_set</span>
    </div>
  </section>

</main>
</body>
</html>
```